Wine and retail website for a high-end resort community

We are introducing a line of quality wines in the resort community of Tidewater Isle, Massachusetts, USA. The site will detail information about the wine, and online store connected to and external government approved shipper for wine, and additional non-alcoholic retail merchandise sales.

We are planning the site to be driven off the Squarespace platform so I do not believe coding is necessary initially; however, the ability to do sop would be helpful if needed.

Attached are the images/files we have available so far. Please feel free to use stock images in your design.

Target Market(s)

Wine enthusiasts in the resort community of Martha’s Vineyard Massachusetts

Industry/Entity Type

Wine

Number of Pages Required

4 page

Font styles to use
Sans Serif

Requirements
Must have
• Home page, about page, wine page, e-commerce page, retail merchandise page. I recently came across brelmorcellars.com and really like the look and layout of their pages if that helps
Nice to have
• A short wine/Martha’s Vineyard related video on the home page

```html
<!DOCTYPE html>
<html lang="en">
<head>
<meta charset="utf-8">
<title>Tidewater Isle – Enjoy Your Moment</title>
<link rel="stylesheet" href="https://fonts.googleapis.com/css2?family=Figtree:wght@400;500;600&family=Libre+Caslon+Text:wght@400;700&display=swap">
<style>
:root{
  --wine:#8b2636;
  --wine-dark:#6f1d2a;
  --band:#8d2b39;
  --ink:#1c1c1c;
  --body:#3a3a3a;
  --soft:#f1f1f1;
  --line:#c98a93;
  --footer:#1d1b1c;
  --white:#ffffff;
}
*{box-sizing:border-box;margin:0;padding:0}
html,body{width:1200px;height:4122px;overflow:hidden;background:var(--white)}
body{position:relative;font-family:"Figtree",sans-serif;color:var(--body)}
.serif{font-family:"Libre Caslon Text",serif}
.abs{position:absolute}

/* header */
.site-header{position:absolute;left:0;top:0;width:1200px;height:106px;background:var(--white)}
.main-nav{position:absolute;left:85px;top:44px;display:flex;gap:31px;font-size:13px;color:var(--ink)}
.brand{position:absolute;left:500px;top:34px;width:200px;text-align:center;font-family:"Libre Caslon Text",serif;font-size:22px;color:#2a2a2a;line-height:1.05;letter-spacing:.5px}
.icon-btn{position:absolute;top:29px;width:45px;height:45px;border:2px solid var(--wine);background:var(--wine);outline:1px solid var(--wine);outline-offset:2px;display:flex;align-items:center;justify-content:center}
.call{position:absolute;left:976px;top:36px;display:flex;gap:10px;align-items:center}
.call small{display:block;font-size:12px;color:var(--ink)}
.call strong{display:block;font-size:14px;font-weight:600;color:var(--ink)}

/* hero */
.hero{position:absolute;left:0;top:106px;width:1200px;height:552px;background:linear-gradient(90deg,#3a3a3a 0%,#5d5d5d 45%,#4c4c4c 100%)}
.hero-photo{position:absolute;left:410px;top:22px;width:780px;height:485px;background:radial-gradient(ellipse at 45% 45%,#a86a3a 0%,#6b3a24 40%,rgba(60,40,30,.0) 75%)}
.hero-tag{position:absolute;left:86px;top:158px;font-size:19px;letter-spacing:7px;color:#efefef}
.hero-title{position:absolute;left:86px;top:196px;font-size:70px;line-height:76px;color:var(--white)}
.btn{position:absolute;display:flex;align-items:center;justify-content:center;background:var(--wine);color:var(--white);font-size:12.5px;font-weight:500;letter-spacing:.3px;outline:1.5px solid var(--wine);outline-offset:3px;border:1.5px solid #fff}
.dots{position:absolute;left:553px;top:526px;display:flex;gap:10px}
.dots i{display:block;width:25px;height:3px;background:#fff}
.dots i.on{background:var(--wine)}

/* about */
.about-title{position:absolute;left:86px;top:745px;font-size:52px;line-height:59px;color:var(--ink)}
.about-title .rule{display:inline-block;width:85px;height:3px;background:var(--wine);vertical-align:middle;margin-left:6px}
.about-text{position:absolute;left:86px;top:880px;width:482px;font-size:16px;line-height:30px}
.video{position:absolute;left:622px;top:768px;width:492px;height:334px;background:linear-gradient(135deg,#3a2818 0%,#6b4a2c 40%,#2b1e14 100%);box-shadow:0 22px 30px rgba(0,0,0,.12)}
.play{position:absolute;left:213px;top:136px;width:62px;height:62px;border-radius:50%;background:#fff}
.progress{position:absolute;left:14px;top:289px;width:464px;height:3px;background:#d9d9d9}
.progress span{display:block;width:152px;height:3px;background:#fff}
.controls{position:absolute;left:14px;top:302px;width:464px;display:flex;align-items:center;gap:22px;color:#fff;font-size:10px}
.leaf-deco{position:absolute;opacity:.5}

/* wines */
.section-title{position:absolute;left:0;width:1200px;text-align:center;font-size:52px;color:var(--ink)}
.section-title .rule{display:inline-block;width:85px;height:3px;background:var(--wine);vertical-align:middle;margin:0 12px}
.wine-photo{position:absolute}
.wine-card{position:absolute;background:var(--soft);padding:40px 42px}
.wine-card h3{font-family:"Libre Caslon Text",serif;font-weight:400;font-size:29px;color:var(--ink);letter-spacing:.5px}
.wine-card p{margin-top:12px;font-size:15.5px;line-height:30px;width:480px}
.stock{position:absolute;font-size:10px;color:var(--ink)}
.price{position:absolute;font-family:"Libre Caslon Text",serif;font-size:29px;color:var(--ink)}
.badge{position:absolute;width:76px;height:76px;border-radius:50%;background:var(--wine);color:#fff;display:flex;align-items:center;justify-content:center;font-size:19px;font-style:italic;font-weight:600;transform:rotate(-12deg)}

/* merch */
.merch{position:absolute;left:0;top:2382px;width:1200px;height:749px;background:var(--band)}
.merch .section-title{top:84px;color:#fff;font-size:50px}
.merch .section-title .rule{background:#fff;width:80px}
.tile{position:absolute;width:330px;height:221px}

/* features */
.features{position:absolute;left:106px;top:3278px;width:988px;height:268px;border:1.5px solid var(--line);display:flex}
.feature{flex:1;position:relative;text-align:center;border-right:1.5px solid var(--line)}
.feature:last-child{border-right:0}
.feature .circle{position:absolute;left:50%;top:-48px;margin-left:-60px;width:120px;height:120px;border-radius:50%;background:var(--wine);display:flex;align-items:center;justify-content:center}
.feature h4{position:absolute;top:108px;width:100%;font-family:"Libre Caslon Text",serif;font-weight:400;font-size:23px;color:var(--ink)}
.feature p{position:absolute;top:145px;left:40px;right:40px;font-size:15.5px;line-height:30px}

/* footer */
.site-footer{position:absolute;left:0;top:3645px;width:1200px;height:477px;background:radial-gradient(ellipse at 75% 40%,#333 0%,var(--footer) 60%)}
.foot-brand{position:absolute;left:120px;top:135px;width:200px;text-align:center;font-family:"Libre Caslon Text",serif;font-size:30px;line-height:1.05;color:#fff}
.newsletter{position:absolute;left:86px;top:246px;display:flex}
.newsletter .field{width:220px;height:43px;background:#fff;font-size:14px;color:#555;padding:13px 16px}
.newsletter .go{width:51px;height:43px;background:var(--wine);display:flex;align-items:center;justify-content:center}
.foot-col{position:absolute;top:92px;color:#fff}
.foot-col h5{font-family:"Libre Caslon Text",serif;font-weight:700;font-size:16px;letter-spacing:.3px}
.foot-col ul{list-style:none;margin-top:50px}
.foot-col li{font-size:16px;line-height:30px}
.contact-row{position:absolute;left:859px;display:flex;gap:19px;align-items:flex-start;color:#fff;font-size:16px;line-height:30px}
.contact-row .pin{width:50px;height:50px;border-radius:50%;background:var(--wine);display:flex;align-items:center;justify-content:center;flex:none}
.copyright{position:absolute;left:86px;top:407px;color:#fff;font-size:16px}
.social{position:absolute;top:394px;width:46px;height:46px;border-radius:50%;border:1.5px solid var(--wine)}
</style>
</head>
<body>

<header class="site-header">
  <nav class="main-nav"><span>About</span><span>Wine</span><span>Product</span><span>Retail Merchandise</span></nav>
  <div class="brand">TIDEWATER<br>ISLE</div>
  <div class="icon-btn" style="left:846px">
    <svg width="18" height="18" viewBox="0 0 18 18" fill="none" stroke="#fff" stroke-width="1.5"><circle cx="9" cy="6" r="3.5"/><path d="M2.5 16c0-3.5 3-5.5 6.5-5.5s6.5 2 6.5 5.5"/></svg>
  </div>
  <div class="icon-btn" style="left:907px">
    <svg width="22" height="20" viewBox="0 0 22 20" fill="none" stroke="#fff" stroke-width="1.5"><path d="M1 2h3l2.5 11h11l2-8H6"/><circle cx="8" cy="17" r="1.5"/><circle cx="16" cy="17" r="1.5"/></svg>
  </div>
  <div class="call">
    <svg width="24" height="22" viewBox="0 0 24 22" fill="none" stroke="var(--wine)" stroke-width="1.6"><path d="M2 8c0-3 4-5 10-5s10 2 10 5l-4 1-1-3H7L6 9z"/><g fill="var(--wine)" stroke="none"><circle cx="8" cy="14" r="1.3"/><circle cx="12" cy="14" r="1.3"/><circle cx="16" cy="14" r="1.3"/><circle cx="8" cy="18" r="1.3"/><circle cx="12" cy="18" r="1.3"/><circle cx="16" cy="18" r="1.3"/></g></svg>
    <div><small>need to call</small><strong>123-456-7890</strong></div>
  </div>
</header>

<section class="hero">
  <div class="hero-photo" role="img" aria-label="Two glasses of red wine with grapes, framed in the outline of the island"></div>
  <div class="hero-tag serif">TIDEWATER ISLE</div>
  <h1 class="hero-title serif" style="font-weight:400">ENJOY YOUR<br>MOMENT</h1>
  <div class="btn" style="left:86px;top:374px;width:190px;height:45px">VIEW OUR WINE'S</div>
  <div class="dots"><i></i><i class="on"></i><i></i></div>
</section>

<section>
  <h2 class="about-title serif" style="font-weight:400">ABOUT TIDEWATER<br>ISLE<span class="rule"></span></h2>
  <p class="about-text">Lorem ipsum dolor sit ametos consectetur adipisicing elito it sed do eiusmod tempor incididunt ut labore et dolore magna aliqua. Ut enim ad minim veniam, quis nostrud exercitationos ullamco laboris nisi ut aliquip ex ea commodo consequat.Esit duis aute irure dolor in reprehenderit in voluptate velit eso us illum dolore eu fugiat nulla pariatur. Excepteur sint occaecat cupidatat non proident, sunt in culpa qui official.</p>
  <div class="btn" style="left:86px;top:1119px;width:232px;height:47px">LEARN MORE ABOUT US</div>

  <div class="video" role="img" aria-label="Video still of a wine bottle in a wooden crate with glasses and grapes">
    <div class="play"><svg width="62" height="62" viewBox="0 0 62 62"><path d="M27 24l11 7-11 7z" fill="#111"/></svg></div>
    <div class="progress"><span></span></div>
    <div class="controls">
      <svg width="10" height="10"><path d="M1 1l8 4-8 4z" fill="#fff"/></svg>
      <svg width="10" height="10"><rect x="1" y="1" width="3" height="8" fill="#fff"/><rect x="6" y="1" width="3" height="8" fill="#fff"/></svg>
      <svg width="10" height="10"><rect x="1" y="1" width="8" height="8" fill="#fff"/></svg>
      <svg width="10" height="10"><path d="M1 1l6 4-6 4z M8 1h1.5v8H8z" fill="#fff"/></svg>
      <svg width="12" height="10"><path d="M1 3h3l3-2v8L4 7H1z" fill="#fff"/></svg>
      <span style="margin-left:auto">03:47 / 10:00</span>
      <svg width="14" height="14"><circle cx="7" cy="7" r="5" fill="none" stroke="#fff" stroke-width="2.5" stroke-dasharray="3 2"/></svg>
      <svg width="16" height="12"><rect x="1" y="1" width="14" height="10" fill="none" stroke="#fff" stroke-width="1.5"/></svg>
    </div>
  </div>
  <div class="leaf-deco" role="img" aria-label="Line drawing of a grape leaf" style="left:1005px;top:1080px;width:195px;height:355px;background:radial-gradient(ellipse at 60% 50%,#f2f2f2 0%,rgba(255,255,255,0) 70%)"></div>
</section>

<section>
  <h2 class="section-title serif" style="top:1250px;font-weight:400"><span class="rule"></span>OUR WINE<span class="rule"></span></h2>
  <div class="leaf-deco" role="img" aria-label="Line drawing of a grape leaf" style="left:0;top:1650px;width:170px;height:360px;background:radial-gradient(ellipse at 40% 50%,#eeeeee 0%,rgba(255,255,255,0) 70%)"></div>

  <div class="wine-photo" role="img" aria-label="Bottles of red and white wine on black" style="left:104px;top:1360px;width:461px;height:432px;background:radial-gradient(ellipse at 55% 70%,#4a3a2a 0%,#0a0a0a 60%)"></div>
  <div class="wine-card" style="left:531px;top:1448px;width:567px;height:290px">
    <h3>CABERNET SAUVIGNON</h3>
    <p>Lorem ipsum dolor sit ametos consectetur adipisicing elito it sed do eiusmod tempor incididunt ut labore et dolore magna aliquat enim ad minim veniam.</p>
    <div class="stock" style="left:42px;top:199px">IN STOCK</div>
    <div class="price" style="left:42px;top:214px">$540.00</div>
    <div class="btn" style="left:171px;top:199px;width:162px;height:45px">ADD TO CART</div>
  </div>
  <div class="badge" style="left:980px;top:1415px">2022</div>

  <div class="wine-photo" role="img" aria-label="Close-up of two wine bottle labels" style="left:635px;top:1850px;width:463px;height:432px;background:linear-gradient(120deg,#e8e6e2 0%,#cfcac4 45%,#2f3a2f 65%,#e2ddd3 85%)"></div>
  <div class="wine-card" style="left:104px;top:1938px;width:565px;height:289px">
    <h3>CHARDONNAY</h3>
    <p>Lorem ipsum dolor sit ametos consectetur adipisicing elito it sed do eiusmod tempor incididunt ut labore et dolore magna aliquat enim ad minim veniam.</p>
    <div class="stock" style="left:42px;top:199px">IN STOCK</div>
    <div class="price" style="left:42px;top:214px">$540.00</div>
    <div class="btn" style="left:171px;top:199px;width:162px;height:45px">ADD TO CART</div>
  </div>
  <div class="badge" style="left:552px;top:1904px">2022</div>
</section>

<section class="merch">
  <h2 class="section-title serif" style="font-weight:400"><span class="rule"></span>MERCHANDISE SALE<span class="rule"></span></h2>
  <div class="tile" role="img" aria-label="Bottle of grapefruit juice with citrus halves" style="left:86px;top:189px;background:linear-gradient(135deg,#f1efed,#e8b8a0)"></div>
  <div class="tile" role="img" aria-label="Black t-shirt on a hanger" style="left:435px;top:189px;background:radial-gradient(ellipse at 50% 55%,#1a1a1a 0%,#2a2a2a 40%,#4a4a4a 100%)"></div>
  <div class="tile" role="img" aria-label="White water bottle on mint background" style="left:784px;top:189px;background:linear-gradient(135deg,#d6e6e2,#f4f7f6)"></div>
  <div class="tile" role="img" aria-label="Red sports bottle on cream background" style="left:86px;top:429px;background:radial-gradient(ellipse at 50% 50%,#d8363a 0%,#e46050 25%,#f4f0de 55%)"></div>
  <div class="tile" role="img" aria-label="White mug on teal background" style="left:435px;top:429px;background:radial-gradient(ellipse at 45% 50%,#f2f4f2 0%,#cfe7df 35%,#7ecbb8 70%)"></div>
  <div class="tile" role="img" aria-label="Red and white trucker caps" style="left:784px;top:429px;background:linear-gradient(135deg,#ececec,#e24a4a 50%,#f2f2f2 75%,#2a2a2a)"></div>
</section>

<section class="features">
  <div class="feature">
    <div class="circle"><svg width="40" height="56" viewBox="0 0 40 56" fill="none" stroke="#fff" stroke-width="2"><path d="M8 3h24c2 12 0 24-12 24S6 15 8 3z"/><path d="M8 12h24"/><path d="M20 27v22M11 52h18"/></svg></div>
    <h4>PROVIDE BEST WINE</h4>
    <p>Lorem ipsum dolor sit ametos dipisicing elito it sed do eiusm mod tempor esia</p>
  </div>
  <div class="feature">
    <div class="circle"><svg width="70" height="40" viewBox="0 0 70 40"><rect x="4" y="6" width="40" height="24" fill="#fff"/><path d="M46 14h12l8 9v7H46z" fill="#fff"/><circle cx="16" cy="33" r="5" fill="#fff" stroke="var(--wine)" stroke-width="2"/><circle cx="56" cy="33" r="5" fill="#fff" stroke="var(--wine)" stroke-width="2"/><text x="24" y="23" text-anchor="middle" font-family="Figtree,sans-serif" font-size="12" font-weight="600" fill="var(--wine)">FREE</text></svg></div>
    <h4>SHIPMENT FREE</h4>
    <p>Lorem ipsum dolor sit ametos dipisicing elito it sed do eiusm mod tempor esia</p>
  </div>
  <div class="feature">
    <div class="circle"><svg width="46" height="52" viewBox="0 0 46 52" fill="#fff"><circle cx="12" cy="16" r="5"/><circle cx="23" cy="16" r="5"/><circle cx="34" cy="16" r="5"/><circle cx="17" cy="26" r="5"/><circle cx="29" cy="26" r="5"/><circle cx="23" cy="36" r="5"/><circle cx="17" cy="45" r="4"/><path d="M23 11V2M23 6c5-4 10-2 12 0" stroke="#fff" stroke-width="2" fill="none"/></svg></div>
    <h4>FARM FRESH PRODUCT</h4>
    <p>Lorem ipsum dolor sit ametos dipisicing elito it sed do eiusm mod tempor esia</p>
  </div>
</section>

<footer class="site-footer">
  <div class="foot-brand">TIDEWATER<br>ISLE</div>
  <div class="newsletter">
    <div class="field">Email..</div>
    <div class="go"><svg width="28" height="12" viewBox="0 0 28 12" fill="none" stroke="#fff" stroke-width="1.5"><path d="M1 6h25M21 1l5 5-5 5"/></svg></div>
  </div>

  <div class="foot-col" style="left:432px">
    <h5>QUICK LINKS</h5>
    <ul><li>About</li><li>Wine</li><li>Product</li><li>Retail Merchandise</li><li>Contact</li></ul>
  </div>
  <div class="foot-col" style="left:654px">
    <h5>OTHER LINKS</h5>
    <ul><li>Login</li><li>Cart</li><li>Wishlist</li><li>Register</li></ul>
  </div>
  <div class="foot-col" style="left:859px"><h5>CONTACT INFORMATION</h5></div>
  <div class="contact-row" style="top:159px">
    <div class="pin"><svg width="14" height="18" viewBox="0 0 14 18"><path d="M7 1a6 6 0 0 1 6 6c0 4-6 10-6 10S1 11 1 7a6 6 0 0 1 6-6z" fill="#fff"/><circle cx="7" cy="7" r="2" fill="var(--wine)"/></svg></div>
    <div>Lito it sed do eiusm mod<br>tempor esia</div>
  </div>
  <div class="contact-row" style="top:236px">
    <div class="pin"><svg width="16" height="16" viewBox="0 0 16 16"><path d="M3 1l3 3-2 2c1 2 4 5 6 6l2-2 3 3-2 2C7 15 1 9 1 3z" fill="#fff"/></svg></div>
    <div style="padding-top:10px">123-456-7890</div>
  </div>

  <div class="copyright">Copyright © 2024 Tidewater Isle. All rights reserved.</div>
  <div class="social" style="left:947px" aria-label="Social link"></div>
  <div class="social" style="left:1006px" aria-label="Social link"></div>
  <div class="social" style="left:1067px" aria-label="Social link"></div>
</footer>

</body>
</html>
```